2m x 3m Trade Show Booth Design

We have a Hospitality Trade Show with a 2m x 3m spot. Two side walls of 2m and one back wall of 3m. Need artwork to be printed on vinyl and attached. Please see attached docs for existing media, logos, etc

```html
<!DOCTYPE html>
<html lang="en">
<head>
<meta charset="utf-8">
<title>VenueMend Trade Show Booth Artwork</title>
<link href="https://fonts.googleapis.com/css2?family=Noto+Sans:wght@400;700;800&family=Oswald:wght@400;500;600&display=swap" rel="stylesheet">
<style>
:root{
  --navy:#0b3868;
  --navy-deep:#082c55;
  --navy-soft:#0e4478;
  --teal:#2bb3ad;
  --teal-dark:#1e8f93;
  --white:#ffffff;
  --stage:#ecebe8;
  --ink:#0b3868;
}
*{box-sizing:border-box;margin:0;padding:0}
html,body{width:1200px;height:791px;overflow:hidden;background:var(--stage)}
body{position:relative;font-family:"Noto Sans",sans-serif;color:var(--white)}
.panel{position:absolute;top:40px;height:348px;background:linear-gradient(160deg,var(--navy-deep),var(--navy) 55%,var(--navy-soft));overflow:hidden}
.side-left{left:24px;width:320px}
.back-wall{left:360px;width:480px}
.side-right{left:856px;width:320px}
.wave{position:absolute;left:0;width:100%;height:40px}
.brand{position:absolute;font-family:"Noto Sans",sans-serif;font-weight:800;color:var(--teal);letter-spacing:-1px;line-height:1}
.brand-line{position:absolute;font-size:8px;white-space:nowrap;color:#1b5a94}
.art{position:absolute;border-radius:8px;background:linear-gradient(180deg,#2bb3ad 0%,#1f7f8f 60%,#0d3f6c 100%);opacity:.9}
/* back wall */
.back-wall .brand{left:20px;top:20px;font-size:36px}
.back-wall .brand-line{left:20px;top:62px}
.headline{position:absolute;left:24px;top:92px;font-weight:800;line-height:1}
.headline .top{display:block;font-size:28px;letter-spacing:1px}
.headline .big{display:block;font-size:40px;color:var(--teal);margin-top:6px;letter-spacing:1px}
.sub{position:absolute;left:24px;top:168px;font-size:14px;line-height:1.2}
.sub b{display:block;font-weight:700}
.back-wall .art{left:304px;top:36px;width:162px;height:224px}
.services{position:absolute;left:16px;top:264px;width:448px;height:60px;background:var(--white);border-radius:10px;display:flex;padding:10px 12px;gap:4px}
.service{flex:1;display:flex;gap:6px;align-items:flex-start}
.service svg{flex:none;width:20px;height:20px}
.service .t{font-size:8px;font-weight:800;color:var(--ink);line-height:1.1}
.service .t small{display:block;font-size:6px;font-weight:700;letter-spacing:.4px;margin-top:2px}
.back-phone{position:absolute;left:24px;top:330px;font-size:10px;font-weight:800}
/* sides */
.side-left .brand{left:18px;top:26px;font-size:30px}
.side-left .brand-line{left:18px;top:62px}
.side-head{position:absolute;font-family:"Oswald",sans-serif;font-weight:600;text-transform:uppercase;font-size:24px;line-height:1.12}
.side-head .accent{color:var(--teal)}
.side-left .side-head{left:18px;top:102px}
.side-left .body{position:absolute;left:18px;top:222px;width:170px;font-family:"Oswald",sans-serif;font-size:11px;line-height:1.35}
.side-left .body b{font-weight:500}
.side-left .art{left:196px;top:172px;width:112px;height:160px}
.call-box{position:absolute;left:18px;top:276px;width:150px;height:50px;background:var(--white);border-radius:8px;padding:8px 10px;font-family:"Oswald",sans-serif}
.call-box .k{font-size:9px;color:var(--teal);letter-spacing:.5px}
.call-box .n{font-size:15px;color:var(--ink);font-weight:500}
.side-right .brand{left:18px;top:26px;font-size:30px}
.side-right .brand-line{left:18px;top:62px}
.side-right .side-head{left:18px;top:102px}
.list{position:absolute;left:18px;top:190px;list-style:none;font-family:"Oswald",sans-serif;font-size:12px;line-height:1.45}
.list li::before{content:"";display:inline-block;width:4px;height:4px;border-radius:50%;background:var(--teal);margin-right:6px;vertical-align:middle}
.info-box{position:absolute;left:18px;top:282px;width:284px;height:54px;background:var(--white);border-radius:8px;padding:6px 12px;font-family:"Oswald",sans-serif;color:var(--ink);line-height:1.3}
.info-box .tag{font-size:12px;font-weight:500}
.info-box .url{font-size:11px;color:var(--teal-dark)}
.info-box .tel{font-size:10px}
/* counter */
.counter{position:absolute;left:425px;top:420px;width:350px;height:190px;background:var(--navy-deep);border-radius:0 0 10px 10px;text-align:center}
.counter-top{position:absolute;left:405px;top:404px;width:390px;height:18px;background:#f6f6f6}
.counter .brand{position:static;display:block;margin-top:30px;font-size:40px}
.counter .brand-line{position:static;display:block;margin-top:6px;font-size:9px}
.counter .phone{margin-top:26px;font-size:17px;font-weight:800}
.counter .url{margin-top:4px;font-size:13px;color:var(--teal)}
</style>
</head>
<body>

<section class="panel side-left">
  <div class="brand">VenueMend</div>
  <div class="brand-line">Hospitality IT, POS &amp; Network Specialists</div>
  <svg class="wave" style="top:74px" viewBox="0 0 320 40" preserveAspectRatio="none"><path d="M0 32 C80 30 150 10 320 4" stroke="var(--teal)" stroke-width="5" fill="none"/><path d="M0 38 C90 34 170 20 320 16" stroke="var(--teal)" stroke-width="1" fill="none"/></svg>
  <h2 class="side-head">Your local<br>hospitality<br><span class="accent">tech support</span><br>team.</h2>
  <p class="body">Hands-on, in-venue support for <b>cafés, restaurants, bars &amp; venues.</b></p>
  <div class="art" role="img" aria-label="Illustrated technician in teal cap and jacket holding a payment terminal"></div>
  <div class="call-box"><div class="k">CALL US</div><div class="n">1300 VENUE1</div></div>
</section>

<section class="panel back-wall">
  <div class="brand">VenueMend</div>
  <div class="brand-line">Hospitality IT, POS &amp; Network Specialists</div>
  <svg class="wave" style="top:68px" viewBox="0 0 480 40" preserveAspectRatio="none"><path d="M0 20 C120 28 240 10 480 18" stroke="var(--teal)" stroke-width="5" fill="none"/><path d="M0 26 C140 32 260 18 480 24" stroke="var(--teal)" stroke-width="1" fill="none"/></svg>
  <h1 class="headline"><span class="top">KEEPING VENUES</span><span class="big">RUNNING.</span></h1>
  <p class="sub"><b>Reliable specialist support</b>when your venue needs it most.</p>
  <div class="art" role="img" aria-label="Illustrated smiling technician with crossed arms holding a payment terminal"></div>
  <div class="services">
    <div class="service"><svg viewBox="0 0 20 20"><circle cx="10" cy="10" r="10" fill="var(--teal)"/><rect x="7" y="5" width="6" height="10" rx="1" fill="none" stroke="#fff" stroke-width="1.4"/></svg><div class="t">POS<small>SUPPORT</small></div></div>
    <div class="service"><svg viewBox="0 0 20 20"><circle cx="10" cy="10" r="10" fill="var(--teal)"/><rect x="6" y="5" width="8" height="10" rx="1" fill="none" stroke="#fff" stroke-width="1.4"/><line x1="8" y1="13" x2="12" y2="13" stroke="#fff"/></svg><div class="t">TABLETS<small>&amp; KIOSKS</small></div></div>
    <div class="service"><svg viewBox="0 0 20 20"><circle cx="10" cy="10" r="10" fill="var(--teal)"/><rect x="5" y="9" width="10" height="5" rx="1" fill="none" stroke="#fff" stroke-width="1.4"/><rect x="7" y="5" width="6" height="4" fill="none" stroke="#fff" stroke-width="1.2"/></svg><div class="t">PRINTERS<small>&amp; PERIPHERALS</small></div></div>
    <div class="service"><svg viewBox="0 0 20 20"><circle cx="10" cy="10" r="10" fill="var(--teal)"/><g stroke="#fff" stroke-width="1.4"><line x1="6" y1="7" x2="14" y2="7"/><line x1="6" y1="10" x2="14" y2="10"/><line x1="6" y1="13" x2="14" y2="13"/></g></svg><div class="t">NETWORK<small>SUPPORT</small></div></div>
    <div class="service"><svg viewBox="0 0 20 20"><circle cx="10" cy="10" r="10" fill="var(--teal)"/><path d="M6 10 A4 4 0 0 1 14 10" fill="none" stroke="#fff" stroke-width="1.4"/><circle cx="10" cy="12" r="1.2" fill="#fff"/></svg><div class="t">ON-SITE<small>TECH SUPPORT</small></div></div>
  </div>
  <div class="back-phone">1300 VENUE1</div>
</section>

<section class="panel side-right">
  <div class="brand">VenueMend</div>
  <div class="brand-line">Hospitality IT, POS &amp; Network Specialists</div>
  <svg class="wave" style="top:74px" viewBox="0 0 320 40" preserveAspectRatio="none"><path d="M0 4 C120 8 200 20 320 34" stroke="var(--teal)" stroke-width="5" fill="none"/><path d="M0 12 C130 16 210 28 320 40" stroke="var(--teal)" stroke-width="1" fill="none"/></svg>
  <h2 class="side-head">Support that<br>understands<br><span class="accent">hospitality.</span></h2>
  <ul class="list">
    <li>POS Support</li>
    <li>Tablets &amp; Kiosks</li>
    <li>Printers &amp; Peripherals</li>
    <li>Networking Support</li>
    <li>On-Site Tech Support</li>
  </ul>
  <div class="info-box"><div class="tag">FAST. PRACTICAL. LOCAL.</div><div class="url">www.venuemend.com.au</div><div class="tel">1300 555 019</div></div>
</section>

<div class="counter-top"></div>
<section class="counter">
  <div class="brand">VenueMend</div>
  <div class="brand-line">Hospitality IT, POS &amp; Network Specialists</div>
  <div class="phone">1300 VENUE1</div>
  <div class="url">venuemend.com.au</div>
</section>

</body>
</html>
```